Cat-products company needs smart, yet endearing, business card

We need a business card design for a new, but up-and-running, business based in Honolulu, Hawaii. The business is Purrlane Nest Co. Our first product is the most environmentally-friendly cat grass kit ever seen on the planet. Future products, currently in the R&D phase, will include a variety of exciting cat scratchers. We also do consulting work to help apartment-dwellers make their home more cat-friendly and, in the future, plan on doing full, custom installs of structure to create high walkways for cats.

Target Market(s)

Middle-aged, apartment-dwelling, middle-class workers who own 1 or more cats and who dote on them.

Industry/Entity Type

Pet Care

Contact Information for Business Card

A striking, professional, yet warm and friendly design is what we're after.

Font styles to use
Serif
Sans Serif
Other font styles liked:
• Comfortaa

Colors

Designer to choose colors to be used in the design.

Requirements
Must have
• The company logo: (see attachment)
• The company name: Purrlane Nest Co
• The web address: www.purrlanenestco.example
• Email: support@purrlanenestco.example
• Phone: +1 (808) 555 0172
• Update (Fri Jun 30 3017 7:45pm Hawaii Time) I would like, is possible, uploaded picture of the cat grass kit on the back of the card with some text along the lines of: Purrlane Nest Co - Where The Freshest Kitty Sprouts Begin
Nice to have
• A cat picture, cartoon, real or silhouette that illustrates cats in action and/or relaxing; ie using the apartment space to live, play and relax in and being well-contented.
• Most of the website is done in the font: Comfortaa. It might be nice to continue using this for brand consistency.
Should not have
• Hard-to-read fonts.

```html
<!DOCTYPE html>
<html lang="en">
<head>
<meta charset="utf-8">
<title>Purrlane Nest Co – Business Card</title>
<link rel="stylesheet" href="https://fonts.googleapis.com/css2?family=Comfortaa:wght@600;700&display=swap">
<style>
  :root {
    --paper: #ffffff;
    --edge: #c4c4c4;
    --ink: #3b3a3a;
    --brown: #5a3128;
    --amber: #f6ae1d;
    --leaf: #6c9a39;
    --leaf-soft: #a9c46f;
    --kraft: #dccdae;
    --coal: #2f2f2f;
  }
  html, body {
    margin: 0;
    width: 1200px;
    height: 328px;
    overflow: hidden;
    background: var(--paper);
    font-family: "Comfortaa", sans-serif;
  }
  .card {
    position: absolute;
    top: 0;
    height: 326px;
    background: var(--paper);
    border: 1px solid var(--edge);
    overflow: hidden;
    box-sizing: border-box;
  }
  .card--front { left: 0; width: 573px; }
  .card--back { left: 628px; width: 566px; }

  .art { position: absolute; }
  .art--cat-dark { left: 0; top: 21px; width: 64px; height: 82px; background: var(--coal); border-radius: 0 40px 40px 0; }
  .art--cat-amber { right: 0; top: 129px; width: 63px; height: 81px; background: var(--amber); border-radius: 40px 0 0 40px; }
  .art--cat-brown { right: 0; top: 219px; width: 69px; height: 90px; background: var(--brown); border-radius: 44px 0 0 44px; }
  .art--grass { bottom: 0; width: 40px; height: 140px; background: linear-gradient(to top, var(--leaf), var(--leaf-soft) 70%, transparent); }
  .card--front .art--grass { left: 0; }
  .card--back .art--grass { right: 0; }
  .art--kit { width: 64px; border-radius: 4px; background: linear-gradient(135deg, var(--kraft), #c9b68f); }
  .art--kit-top { left: 422px; top: 17px; height: 99px; }
  .art--kit-bottom { left: 448px; top: 129px; height: 94px; }

  .brand {
    position: absolute;
    left: 0; right: 0;
    text-align: center;
  }
  .brand__dot {
    display: block;
    margin: 0 auto 12px;
    width: 48px; height: 48px;
    border-radius: 50%;
    background: var(--brown);
  }
  .brand__name { font-weight: 700; color: var(--amber); font-size: 27px; }
  .card--front .brand { top: 34px; }
  .card--back .brand { top: 115px; left: 60px; right: 150px; }
  .card--back .brand__name { color: var(--brown); font-size: 31px; }

  .contact {
    position: absolute;
    left: 0; right: 0;
    text-align: center;
    font-weight: 700;
    margin: 0;
  }
  .contact--web { top: 182px; font-size: 25px; color: var(--ink); }
  .contact--mail, .contact--phone { display: flex; justify-content: center; align-items: center; gap: 8px; }
  .contact--mail { top: 226px; font-size: 18px; color: var(--amber); }
  .contact--phone { top: 264px; font-size: 18px; color: var(--brown); }
  .icon { width: 26px; height: 26px; flex: none; }

  .tagline {
    position: absolute;
    top: 200px;
    left: 100px; right: 150px;
    margin: 0;
    text-align: center;
    font-weight: 700;
    font-size: 20px;
    line-height: 32px;
    color: var(--brown);
  }
  .tagline__green { color: var(--leaf); }
  .tagline__amber { color: var(--amber); }
</style>
</head>
<body>
  <section class="card card--front">
    <div class="art art--cat-dark" role="img" aria-label="Black cat peeking in from the corner"></div>
    <div class="art art--cat-amber" role="img" aria-label="Orange cat peeking in from the side"></div>
    <div class="art art--cat-brown" role="img" aria-label="Brown cat peeking in from the side"></div>
    <div class="art art--grass" role="img" aria-label="Blades of cat grass"></div>

    <div class="brand">
      <span class="brand__dot"></span>
      <span class="brand__name">Purrlane Nest Co</span>
    </div>

    <p class="contact contact--web">www.purrlanenestco.example</p>
    <p class="contact contact--mail">
      <svg class="icon" viewBox="0 0 26 26" aria-hidden="true">
        <circle cx="13" cy="13" r="13" fill="#3b3a3a"/>
        <rect x="6.5" y="8.5" width="13" height="9" fill="#fff"/>
        <path d="M6.5 8.5 L13 14 L19.5 8.5" fill="none" stroke="#3b3a3a" stroke-width="1.4"/>
      </svg>
      support@purrlanenestco.example
    </p>
    <p class="contact contact--phone">
      <svg class="icon" viewBox="0 0 26 26" aria-hidden="true">
        <circle cx="13" cy="13" r="11.5" fill="none" stroke="#3b3a3a" stroke-width="2"/>
        <path d="M9 7.5 L11 7.5 L12 10.5 L10.6 11.6 Q12 14.6 14.4 15.4 L15.5 14 L18.5 15 L18.5 17 Q18 18.5 16 18.5 Q8 17 7.5 10 Q7.5 8 9 7.5 Z" fill="#3b3a3a"/>
      </svg>
      +1 (808) 555 0172
    </p>
  </section>

  <section class="card card--back">
    <div class="art art--kit art--kit-top" role="img" aria-label="Cat grass kit box"></div>
    <div class="art art--kit art--kit-bottom" role="img" aria-label="Cat grass kit box, side view"></div>
    <div class="art art--grass" role="img" aria-label="Blades of cat grass"></div>

    <div class="brand">
      <span class="brand__name">Purrlane Nest Co</span>
    </div>

    <p class="tagline">
      Where the <span class="tagline__green">FRESHEST</span> Kitty<br>
      Sprouts <span class="tagline__amber">BEGIN</span>!
    </p>
  </section>
</body>
</html>
```